KRD Website Photoshop

Our client is a security locksmith business on the Gold Coast in Australia. They have an existing website www.krdsecurity.com.au that they would like redesigned.

The website will be built on Dot net nuke so the design needs to ensure follows their skinning standards.
Updates

Hi everyone

Apologies for the delay....our client went overseas and won't be back until the new year....so will let you know feedback then.

Cheers
Maya

Target Market(s)

General public

Industry/Entity Type

Security

Number of Pages Required

1 page

Requirements
Must have
• Client would like the below revisions:

1. The banner image is too large and they would like to make it smaller.

2. Several call to action buttons like:

- Locksmiths
- Electronic Security
- Door Hardware

They would like to make the KRD logo smaller and make the word eg: LOCKSMITHS to be larger and the feature in the button. (have attached the logos)

There will also need to be a Book a Job button featured.

Homepage banner will include phone number and logo

```html
<!DOCTYPE html>
<html lang="en">
<head>
<meta charset="utf-8">
<title>KRD Security Solutions</title>
<link rel="stylesheet" href="https://fonts.googleapis.com/css2?family=Arimo:wght@400;700&display=swap">
<style>
  :root {
    --maroon: #7d1a36;
    --maroon-dark: #5e0f26;
    --maroon-deep: #4a0b1d;
    --crimson: #a3223f;
    --sky: #d6eaf8;
    --sky-light: #eef6fc;
    --ink: #3b3b3b;
    --heading: #a3223f;
    --teal: #0f5e80;
    --white: #ffffff;
  }
  * { box-sizing: border-box; margin: 0; padding: 0; }
  html, body { width: 1200px; height: 1076px; overflow: hidden; }
  body {
    position: relative;
    background: linear-gradient(180deg, #8e2544 0%, var(--maroon) 55%, var(--maroon-dark) 100%);
    font-family: "Arimo", Arial, sans-serif;
    color: var(--ink);
  }
  a { text-decoration: none; }
  .site {
    position: absolute; left: 12px; top: 66px; width: 1164px; height: 914px;
    background: linear-gradient(180deg, var(--sky) 50%, var(--sky-light) 100%);
    border-radius: 10px; overflow: hidden;
  }
  .main-nav {
    height: 37px; display: flex; align-items: center; padding-left: 20px;
    background: linear-gradient(180deg, #a32a4b, var(--maroon));
  }
  .main-nav a {
    color: var(--white); font-weight: 700; font-size: 15px;
    padding: 0 16px; height: 37px; line-height: 37px;
    border-right: 1px solid rgba(255,255,255,0.15);
  }
  .main-nav a:last-child { border-right: none; }
  .hero { position: absolute; top: 37px; left: 0; width: 1164px; height: 339px; display: flex; }
  .hero-photo {
    width: 731px; height: 339px;
    background: linear-gradient(160deg, #c9c9c9 0%, #7a7a7a 45%, #3e3e3e 100%);
  }
  .hero-brand {
    position: relative; width: 433px; height: 339px;
    background: linear-gradient(135deg, #8e2544, var(--maroon-dark));
  }
  .brand-name {
    position: absolute; left: 0; top: 98px; width: 433px; text-align: center;
    color: var(--white); font-size: 54px; font-weight: 700; line-height: 60px;
  }
  .brand-tag {
    position: absolute; left: 0; top: 166px; width: 433px; text-align: center;
    color: var(--white); font-size: 15px; font-weight: 700; letter-spacing: 2px;
  }
  .phone-bar {
    position: absolute; left: 0; bottom: 0; width: 433px; height: 64px;
    background: var(--maroon-deep); display: flex; align-items: center; padding-left: 30px; gap: 14px;
  }
  .phone-bar span { color: var(--white); font-size: 22px; font-weight: 700; letter-spacing: 0.5px; }
  .cards { position: absolute; top: 423px; left: 0; width: 100%; }
  .card {
    position: absolute; top: 0; width: 335px; height: 223px;
    background: radial-gradient(circle at 50% 40%, #ffffff 60%, #eeeeee 100%);
    border: 3px solid #f2f7fb; box-shadow: 0 0 3px rgba(0,0,0,0.12);
  }
  .card .name {
    position: absolute; left: 0; top: 42px; width: 100%; text-align: center;
    font-size: 48px; font-weight: 700; color: var(--ink); line-height: 60px;
  }
  .card .button {
    position: absolute; left: 28px; top: 150px; width: 283px; height: 49px; border-radius: 10px;
    color: var(--white); font-weight: 700; font-size: 17px; text-align: center; line-height: 49px;
    letter-spacing: 0.5px;
  }
  .card-locksmiths { left: 51px; }
  .card-locksmiths .button { background: linear-gradient(180deg, #c0486a, #8e1f40); color: #f3d9e1; }
  .card-electronic { left: 416px; }
  .card-electronic .button { background: linear-gradient(180deg, #c8b52a, #93850f); }
  .card-architectural { left: 770px; }
  .card-architectural .button { background: linear-gradient(180deg, #1b7399, var(--teal)); }
  .panel {
    position: absolute; top: 689px; height: 193px;
    background: linear-gradient(180deg, #e6e3e6 0%, #ffffff 45%);
  }
  .panel h2 { color: var(--heading); font-size: 23px; font-weight: 700; }
  .panel p { font-size: 15px; line-height: 22px; }
  .about { left: 32px; width: 752px; padding: 24px 26px; }
  .about h2 { margin-bottom: 12px; }
  .about p + p { margin-top: 22px; }
  .about a { color: var(--maroon); }
  .employment { left: 794px; width: 345px; padding: 20px 30px; }
  .employment h2 { margin-bottom: 4px; }
  .book-job {
    display: inline-block; margin-top: 11px; width: 155px; height: 37px; border-radius: 7px;
    background: linear-gradient(180deg, #b0355a, #7a1733); color: var(--white);
    font-weight: 700; font-size: 17px; text-align: center; line-height: 37px;
  }
  .footer-nav {
    position: absolute; top: 996px; left: 0; width: 100%;
    display: flex; justify-content: center; gap: 33px; padding-left: 20px;
  }
  .footer-nav a { color: #f0d6de; font-weight: 700; font-size: 15px; }
  .copyright {
    position: absolute; top: 1033px; left: 0; width: 100%; text-align: center;
    color: var(--white); font-weight: 700; font-size: 12px; padding-left: 18px;
  }
</style>
</head>
<body>
  <div class="site">
    <nav class="main-nav">
      <a href="#">Home</a>
      <a href="#">Locksmiths</a>
      <a href="#">Electronic Security</a>
      <a href="#">Architectural Hardware</a>
      <a href="#">About</a>
      <a href="#">Location</a>
      <a href="#">Contact KRD</a>
      <a href="#">Employment</a>
    </nav>

    <header class="hero">
      <div class="hero-photo" role="img" aria-label="Team photo of the KRD staff standing in front of the company's white service vans"></div>
      <div class="hero-brand">
        <p class="brand-name">KRD</p>
        <p class="brand-tag">SECURITY SOLUTIONS</p>
        <div class="phone-bar">
          <svg width="48" height="48" viewBox="0 0 48 48" aria-hidden="true">
            <rect x="6" y="4" width="36" height="40" rx="8" fill="#e8e8e8" stroke="#bbb"/>
            <rect x="14" y="10" width="20" height="7" fill="#a8c8e0"/>
            <g fill="#d9334a">
              <circle cx="17" cy="24" r="2.3"/><circle cx="24" cy="24" r="2.3"/><circle cx="31" cy="24" r="2.3"/>
              <circle cx="17" cy="31" r="2.3"/><circle cx="24" cy="31" r="2.3"/><circle cx="31" cy="31" r="2.3"/>
              <circle cx="17" cy="38" r="2.3"/><circle cx="24" cy="38" r="2.3"/><circle cx="31" cy="38" r="2.3"/>
            </g>
          </svg>
          <span>Tel :(07) 5500 0123</span>
        </div>
      </div>
    </header>

    <section class="cards">
      <div class="card card-locksmiths">
        <p class="name">KRD</p>
        <a class="button" href="#">LOCKSMITHS</a>
      </div>
      <div class="card card-electronic">
        <p class="name">KRD</p>
        <a class="button" href="#">ELECTRONIC SECURITY</a>
      </div>
      <div class="card card-architectural">
        <p class="name">KRD</p>
        <a class="button" href="#">ARCHITECTURAL SOLUTIONS</a>
      </div>
    </section>

    <section class="panel about">
      <h2>About KRD</h2>
      <p>Established in 1990, KRD Security Solutions has grown from a mobile locksmith van into the Gold Coast's largest and most comprehensive locksmith and security services provider.</p>
      <p>Founder and managing director Daniel Morrow, KRD partners Paul Kessing and Leo Hartley and more than 45 staff <a href="#">(view more)</a></p>
    </section>

    <section class="panel employment">
      <h2>Employment</h2>
      <p>KRD Security is currently seeking skilled professionals in the field of Electronic Security.</p>
      <a class="book-job" href="#">Book a Job</a>
    </section>
  </div>

  <nav class="footer-nav">
    <a href="#">Home</a>
    <a href="#">Locksmiths</a>
    <a href="#">Electronic Security</a>
    <a href="#">Architectural Hardware</a>
    <a href="#">About</a>
    <a href="#">Location</a>
    <a href="#">Contact KRD</a>
    <a href="#">Employment</a>
  </nav>
  <p class="copyright">Copyright © Security Solution 2009</p>
</body>
</html>
```